Baseball Themed Birthday Invitation

Hello,

I need a birthday invitation design created for me. I will be taking the design, getting it manufactured in bulk and selling them.

These types of invitations are not custom, but rather will have "fill in fields". Please see attachment as an example (wild one example attached). The mandatory fill in fields are : Name, Location, Date, Time, RSVP.

The target age will be 4-12

The size is 7" x 5".

This project is for a Baseball themed party design. I attached an example invitation (baseball design) to show one i really like. This design does not include the fill in fields, but i like the use of fonts/colors design. That being said, I am open to seeing different concepts and designs.

Thank you!

Target Market(s)

Boys 4-12 years old

Requirements
Must have
• Fill in fields as discussed in brief.

```html
<!DOCTYPE html>
<html lang="en">
<head>
<meta charset="utf-8">
<title>Wild One Baseball Birthday Invitation</title>
<link rel="stylesheet" href="https://fonts.googleapis.com/css2?family=Graduate&family=Lobster&family=Oswald:wght@600;700&display=block">
<style>
  :root {
    --navy: #2a3990;
    --red: #c8202f;
    --red-light: #e0525c;
    --cream: #f1e5cf;
    --white: #ffffff;
  }
  html, body {
    margin: 0;
    padding: 0;
    width: 1200px;
    height: 857px;
    overflow: hidden;
    background: var(--white);
  }
  .invitation { display: block; width: 1200px; height: 857px; }
  .script-line {
    font-family: "Lobster", "Brush Script MT", cursive;
    fill: var(--red);
  }
  .varsity {
    font-family: "Graduate", "Rockwell Extra Bold", "Rockwell", serif;
  }
  .varsity-outline {
    fill: var(--red);
    stroke: var(--red);
    stroke-width: 14;
    stroke-linejoin: miter;
  }
  .varsity-inline {
    fill: var(--white);
    stroke: var(--white);
    stroke-width: 8;
    stroke-linejoin: miter;
  }
  .varsity-face { fill: url(#halftone); }
  .field-label, .field-value, .age-number {
    font-family: "Oswald", "Arial Narrow", sans-serif;
    font-weight: 700;
    fill: var(--navy);
  }
  .field-label { font-weight: 600; }
  .field-label.block-label { font-family: "Graduate", "Rockwell", serif; font-weight: 400; }
</style>
</head>
<body>
<svg class="invitation" viewBox="0 0 1200 857" xmlns="http://www.w3.org/2000/svg">
  <defs>
    <radialGradient id="sunburst-tone" cx="0.5" cy="0.9" r="0.8">
      <stop offset="0" stop-color="#fbfbf9"/>
      <stop offset="1" stop-color="#dcdde1"/>
    </radialGradient>
    <linearGradient id="batter-tone" x1="0" y1="0" x2="0" y2="1">
      <stop offset="0" stop-color="#e3e6f3"/>
      <stop offset="1" stop-color="#b4bbdc"/>
    </linearGradient>
    <pattern id="halftone" width="6" height="6" patternUnits="userSpaceOnUse">
      <rect width="6" height="6" fill="var(--red)"/>
      <circle cx="3" cy="3" r="1.1" fill="var(--red-light)"/>
    </pattern>
  </defs>

  <!-- frame -->
  <rect class="frame" x="0" y="0" width="1200" height="857" fill="var(--navy)"/>

  <!-- stage background -->
  <rect class="sunburst" x="33" y="33" width="1133" height="530" fill="url(#sunburst-tone)"
        role="img" aria-label="Grey and white sunburst rays radiating from the centre"/>

  <!-- stitching -->
  <polygon class="stitching" points="33,265 33,295 240,38 205,34" fill="#ecc3c7"
           role="img" aria-label="Red baseball seam stitching along the upper left corner"/>
  <polygon class="stitching" points="1166,265 1166,295 960,38 995,34" fill="#ecc3c7"
           role="img" aria-label="Red baseball seam stitching along the upper right corner"/>

  <!-- bunting -->
  <polygon class="bunting" points="234,34 966,34 966,62 600,108 234,62" fill="#e3c8d2"
           role="img" aria-label="Red and blue patterned pennant bunting strung across the top"/>

  <!-- batters -->
  <polygon class="batter" points="45,420 120,330 210,312 215,400 229,563 85,563" fill="url(#batter-tone)"
           role="img" aria-label="Blue line illustration of a young batter ready to swing"/>
  <polygon class="batter" points="1155,420 1080,330 990,312 985,400 971,563 1115,563" fill="url(#batter-tone)"
           role="img" aria-label="Blue line illustration of a young batter ready to swing, mirrored"/>

  <!-- heading -->
  <text class="script-line" x="605" y="172" font-size="76" text-anchor="middle"
        textLength="466" lengthAdjust="spacingAndGlyphs" transform="rotate(4 605 150)">Its Going to be a</text>

  <rect class="rule" x="339" y="211" width="213" height="5" fill="var(--red)"/>
  <rect class="rule" x="647" y="211" width="214" height="5" fill="var(--red)"/>
  <g class="trophy" fill="var(--navy)">
    <path d="M585 187 H615 V195 Q615 214 600 218 Q585 214 585 195 Z"/>
    <path d="M585 191 Q577 191 579 199 Q581 206 587 207" fill="none" stroke="var(--navy)" stroke-width="2.5"/>
    <path d="M615 191 Q623 191 621 199 Q619 206 613 207" fill="none" stroke="var(--navy)" stroke-width="2.5"/>
    <rect x="598" y="217" width="4" height="9"/>
    <rect x="592" y="226" width="16" height="4"/>
    <rect x="589" y="230" width="22" height="11"/>
  </g>

  <g class="headline varsity" font-size="150" text-anchor="middle">
    <text class="varsity-outline" x="587" y="356" textLength="715" lengthAdjust="spacingAndGlyphs">WILD ONE</text>
    <text class="varsity-inline" x="587" y="356" textLength="715" lengthAdjust="spacingAndGlyphs">WILD ONE</text>
    <text class="varsity-face" x="587" y="356" textLength="715" lengthAdjust="spacingAndGlyphs">WILD ONE</text>
  </g>

  <g class="ball">
    <circle cx="305" cy="394" r="17" fill="var(--white)" stroke="var(--red)" stroke-width="3"/>
    <path d="M296 381 Q304 394 296 407 M314 381 Q306 394 314 407" fill="none" stroke="var(--red)" stroke-width="2"/>
  </g>
  <g class="ball">
    <circle cx="895" cy="394" r="17" fill="var(--white)" stroke="var(--red)" stroke-width="3"/>
    <path d="M886 381 Q894 394 886 407 M904 381 Q896 394 904 407" fill="none" stroke="var(--red)" stroke-width="2"/>
  </g>
  <text class="script-line" x="600" y="410" font-size="58" text-anchor="middle"
        textLength="512" lengthAdjust="spacingAndGlyphs">Join to use the Celebrate</text>

  <g class="headline varsity" font-size="150" text-anchor="middle">
    <text class="varsity-outline" x="597" y="538" textLength="394" lengthAdjust="spacingAndGlyphs">NAME</text>
    <text class="varsity-inline" x="597" y="538" textLength="394" lengthAdjust="spacingAndGlyphs">NAME</text>
    <text class="varsity-face" x="597" y="538" textLength="394" lengthAdjust="spacingAndGlyphs">NAME</text>
  </g>

  <!-- details panel -->
  <rect class="divider-band" x="33" y="563" width="1133" height="9" fill="var(--red)"/>
  <rect class="details" x="33" y="572" width="1133" height="251" fill="var(--cream)"/>

  <line x1="337" y1="577" x2="337" y2="817" stroke="var(--navy)" stroke-width="8" stroke-dasharray="8 22"/>
  <line x1="863" y1="577" x2="863" y2="817" stroke="var(--navy)" stroke-width="8" stroke-dasharray="8 22"/>

  <g class="field-date">
    <text class="field-label" x="183" y="621" font-size="40" text-anchor="middle"
          textLength="124" lengthAdjust="spacingAndGlyphs">DATE :</text>
    <text class="field-value" x="183" y="688" font-size="68" text-anchor="middle"
          textLength="252" lengthAdjust="spacingAndGlyphs">00/00/00</text>
  </g>
  <g class="field-time">
    <text class="field-label" x="176" y="741" font-size="40" text-anchor="middle"
          textLength="110" lengthAdjust="spacingAndGlyphs">TIME :</text>
    <text class="field-value" x="174" y="805" font-size="66" text-anchor="middle"
          textLength="152" lengthAdjust="spacingAndGlyphs">00:00</text>
  </g>
  <g class="field-rsvp">
    <text class="field-label block-label" x="594" y="622" font-size="40" text-anchor="middle"
          textLength="140" lengthAdjust="spacingAndGlyphs">RSVP :</text>
    <text class="field-value" x="595" y="682" font-size="60" text-anchor="middle"
          textLength="364" lengthAdjust="spacingAndGlyphs">000-000-0000</text>
  </g>
  <g class="field-location">
    <text class="field-label" x="594" y="745" font-size="46" text-anchor="middle"
          textLength="224" lengthAdjust="spacingAndGlyphs">LOCATION :</text>
    <line x1="377" y1="790" x2="825" y2="790" stroke="var(--navy)" stroke-width="6" stroke-dasharray="5 3"/>
  </g>
  <g class="field-age">
    <text class="field-label" x="1020" y="621" font-size="36" text-anchor="middle"
          textLength="98" lengthAdjust="spacingAndGlyphs">YEARS</text>
    <text class="age-number" x="1024" y="786" font-size="178" text-anchor="middle"
          textLength="186" lengthAdjust="spacingAndGlyphs">00</text>
  </g>
</svg>
</body>
</html>
```